Bref créative
Logo for coaching business
Bus card design, stationary/letterhead, envelopes
Professional
Gerald Pinsky
International Author - Coach - Mentor
20583 W. Marigold Ave. #215-347
Scottsdale, AZ 85917
Gerald@brightkestrelcoaching.example
www.BrightKestrelCoaching.example
Need additional bus. card layout for-
Tom Ridgely, MMAC
Life Coach - Counselor
Tom@brightkestrelcoaching.example

```html
<!DOCTYPE html>
<html lang="en">
<head>
<meta charset="utf-8">
<title>Bright Kestrel Coaching – Business Card</title>
<link rel="stylesheet" href="https://fonts.googleapis.com/css2?family=Cinzel:wght@400;600&display=swap">
<style>
  :root {
    --page-bg: #e9e7e4;
    --card-bg: #ffffff;
    --ink-dark: #3b3b3d;
    --ink-soft: #6a6a6e;
    --accent-blue: #2f6fae;
    --icon-bg: #2f6fae;
    --icon-fg: #ffffff;
    --card-shadow: rgba(0, 0, 0, 0.18);
  }
  * { box-sizing: border-box; margin: 0; padding: 0; }
  html, body {
    width: 1200px;
    height: 900px;
    overflow: hidden;
    background: var(--page-bg);
    font-family: "Cinzel", "Times New Roman", serif;
  }
  .business-card {
    position: absolute;
    left: 100px;
    top: 164px;
    width: 1000px;
    height: 572px;
    background: var(--card-bg);
    box-shadow: 0 10px 30px var(--card-shadow);
  }
  .brand {
    position: absolute;
    left: 110px;
    top: 92px;
    display: flex;
    align-items: center;
    gap: 26px;
  }
  .brand-dot {
    width: 86px;
    height: 86px;
    border-radius: 50%;
    background: var(--accent-blue);
    flex: none;
  }
  .brand-name {
    font-size: 46px;
    font-weight: 400;
    color: var(--ink-dark);
    letter-spacing: 1px;
    line-height: 1;
  }
  .brand-tagline {
    margin-top: 12px;
    font-size: 14px;
    letter-spacing: 2px;
    color: var(--ink-soft);
    text-transform: uppercase;
  }
  .person {
    position: absolute;
    left: 0;
    right: 0;
    top: 268px;
    text-align: center;
  }
  .person-name {
    font-size: 22px;
    font-weight: 600;
    color: var(--accent-blue);
    letter-spacing: 1px;
  }
  .person-title {
    margin-top: 8px;
    font-size: 15px;
    color: var(--ink-soft);
    letter-spacing: 1px;
  }
  .contact {
    position: absolute;
    left: 60px;
    right: 60px;
    bottom: 54px;
    font-size: 15px;
    color: var(--ink-soft);
    letter-spacing: 0.5px;
  }
  .contact-line {
    display: flex;
    align-items: center;
    gap: 10px;
    margin-top: 9px;
  }
  .contact-line .spacer { width: 22px; }
  .contact-icon {
    width: 20px;
    height: 20px;
    flex: none;
  }
  .contact-icon circle.bg { fill: var(--icon-bg); }
  .contact-icon .glyph { fill: none; stroke: var(--icon-fg); stroke-width: 1.4; stroke-linecap: round; stroke-linejoin: round; }
</style>
</head>
<body>
  <article class="business-card">
    <header class="brand">
      <span class="brand-dot"></span>
      <div>
        <div class="brand-name">Bright Kestrel Coaching</div>
        <div class="brand-tagline">New Consciousness · New Awareness · New Life</div>
      </div>
    </header>

    <section class="person">
      <div class="person-name">Gerald Pinsky</div>
      <div class="person-title">International Author - Coach - Mentor</div>
    </section>

    <footer class="contact">
      <div class="contact-line">
        <svg class="contact-icon" viewBox="0 0 20 20" aria-hidden="true">
          <circle class="bg" cx="10" cy="10" r="10"/>
          <path class="glyph" d="M10 15.5 C7 12 6.5 10.5 6.5 8.8 A3.5 3.5 0 0 1 13.5 8.8 C13.5 10.5 13 12 10 15.5 Z"/>
          <circle class="glyph" cx="10" cy="8.8" r="1.2"/>
        </svg>
        <span>20583 W. Marigold Ave. #215-347 Scottsdale, AZ 85917</span>
        <span class="spacer"></span>
        <svg class="contact-icon" viewBox="0 0 20 20" aria-hidden="true">
          <circle class="bg" cx="10" cy="10" r="10"/>
          <circle class="glyph" cx="10" cy="10" r="5.5"/>
          <ellipse class="glyph" cx="10" cy="10" rx="2.4" ry="5.5"/>
          <path class="glyph" d="M4.5 10 H15.5"/>
        </svg>
        <span>www.BrightKestrelCoaching.example</span>
      </div>
      <div class="contact-line">
        <svg class="contact-icon" viewBox="0 0 20 20" aria-hidden="true">
          <circle class="bg" cx="10" cy="10" r="10"/>
          <path class="glyph" d="M7 5 L9 7.5 L7.8 9 C8.6 10.6 9.6 11.6 11 12.3 L12.5 11 L15 13 L13.6 14.8 C9.5 14.5 5.5 10.5 5.2 6.4 Z"/>
        </svg>
        <span>480-555-0142</span>
      </div>
      <div class="contact-line">
        <svg class="contact-icon" viewBox="0 0 20 20" aria-hidden="true">
          <circle class="bg" cx="10" cy="10" r="10"/>
          <rect class="glyph" x="5" y="6.5" width="10" height="7" rx="0.8"/>
          <path class="glyph" d="M5.3 7 L10 10.8 L14.7 7"/>
        </svg>
        <span>Gerald@brightkestrelcoaching.example</span>
      </div>
    </footer>
  </article>
</body>
</html>
```